Business Card Design

I need a Business Card that will catch the attention that will not get thrown in a Drawer. I have 23 companies I use for Auto, Home, Life, and Business Insurance. I make sure that people have the best coverage for the $ spent.

Industry/Entity Type

Business

Contact Information for Business Card

Torvin Insurance Agency, Inc., Derek Halloway, 4735 West Fallow Lane Larkfield Springs 52913 555-287-6194, www.torvinagency-example.com, Facebook, LinkedIn, Google+

```html
<!DOCTYPE html>
<html lang="en">
<head>
<meta charset="utf-8">
<title>Torvin Insurance Agency – Business Card</title>
<link rel="stylesheet" href="https://fonts.googleapis.com/css2?family=Tinos:wght@400;700&family=Questrial&display=swap">
<style>
  :root {
    --backdrop: #1c1c1e;
    --card-frost: #a4a7ab;
    --card-edge: #c3c6ca;
    --panel-blue: #1f6ec6;
    --ink-white: #ffffff;
    --chip: #dfe3e8;
  }
  html, body {
    margin: 0;
    width: 1200px;
    height: 800px;
    overflow: hidden;
    background: var(--backdrop);
  }
  .canvas {
    position: relative;
    width: 1200px;
    height: 800px;
  }
  .card {
    position: absolute;
    left: 180px;
    top: 160px;
    width: 840px;
    height: 480px;
    border-radius: 24px;
    background: linear-gradient(160deg, var(--card-edge), var(--card-frost) 55%, #93969a);
    box-shadow: 0 20px 40px rgba(0,0,0,.5);
    overflow: hidden;
  }
  .panel {
    position: absolute;
    left: 36px;
    top: 48px;
    width: 780px;
    height: 348px;
    background: var(--panel-blue);
    color: var(--ink-white);
  }
  .brand {
    position: absolute;
    left: 34px;
    top: 10px;
  }
  .brand-name {
    margin: 0;
    font-family: "Tinos", serif;
    font-weight: 400;
    font-size: 78px;
    letter-spacing: 4px;
    line-height: 1;
  }
  .brand-tagline {
    margin: 0 0 0 2px;
    font-family: "Questrial", sans-serif;
    font-size: 25px;
    letter-spacing: 1px;
    line-height: 1.1;
  }
  .contact {
    position: absolute;
    right: 40px;
    top: 138px;
    width: 360px;
    text-align: right;
    font-family: "Tinos", serif;
  }
  .rule {
    height: 4px;
    background: var(--ink-white);
  }
  .contact-name {
    margin: 6px 0 4px;
    font-weight: 700;
    font-size: 27px;
    line-height: 1.1;
  }
  .contact-lines {
    margin: 6px 0 0;
    font-size: 23px;
    line-height: 1.33;
  }
  .website {
    position: absolute;
    left: 34px;
    bottom: 22px;
    font-family: "Questrial", sans-serif;
    font-size: 26px;
    letter-spacing: 1.5px;
  }
  .social {
    position: absolute;
    right: 60px;
    bottom: 60px;
    display: flex;
    gap: 6px;
  }
  .social-chip {
    width: 22px;
    height: 22px;
    border-radius: 3px;
    background: var(--chip);
  }
</style>
</head>
<body>
<main class="canvas">
  <article class="card">
    <section class="panel">
      <header class="brand">
        <h1 class="brand-name">TORVIN</h1>
        <p class="brand-tagline">Insurance Agency, Inc.</p>
      </header>
      <div class="contact">
        <div class="rule"></div>
        <p class="contact-name">Derek Halloway</p>
        <div class="rule"></div>
        <p class="contact-lines">
          4735 West Fallow Lane<br>
          Larkfield Springs 52913<br>
          555-287-6194(O)<br>
          555-613-4820(C)
        </p>
      </div>
      <div class="website">www.torvinagency-example.com</div>
    </section>
    <div class="social" aria-label="Social profiles">
      <span class="social-chip"></span>
      <span class="social-chip"></span>
      <span class="social-chip"></span>
    </div>
  </article>
</main>
</body>
</html>
```